KeLta Assembly. "Powering Enterprise Renewal" Website

I have established a new company based in Sydney Australia that exists to support large service companies to transform their businesses. I offer a bespoke alternative to the large consulting firms like RJ, Hartwell, TDRW and Brannock. My intention over time is to grow this business with more consulting partners and practitioners and expand into ASIA PAC, Europe and the US.

I would like to create a mobile responsive website that has a similar look and feel to RJ, see URL below plus URLs for Brannock, Hartwell and TDRW.

http://www.rj-example.com/
https://home.tdrw-example.com/au/en/home.html
http://www.brannock-example.com/

I am on a limited budget however so do not require a whole lot of fancy features. Key priorities;

- Responsive to all device types. PC, Tablet, Mobile
- A horizontal scrolling set of hero images that link to particular story or subject like RJ-example.com. 3 only required
- Only limited content is required and most would be static apart from hero scrolling images/topics at top of page
- I would need the ability to be able to remove, replace, update the hero slides every 3-4 months
- Key priority is to present a level of professionalism and look and feel on par with RJ, Hartwell, Brannock and Co, for people to know what I do and how to contact me.
- Link site to my connect up Profile
- My logo is attached and contact details
- I have purchased the domain name www.keltaassembly-example.com.au through sure names

Industry/Entity Type

Management Consulting

Coding

Coded - Design and coding required

Number of Pages Required

1 page

Requirements
Must have
• Mobile responsive to be viewed on any device, simple clean design, easy to find contact details, 3 scrolling articles like RJ-example.com that link to a PDF article. Align colours and theming to Logo on white background attached. Align fonts, look and feel etc to Log design attached

```html
<!DOCTYPE html>
<html lang="en">
<head>
<meta charset="utf-8">
<title>KeLta Assembly — Testimonials</title>
<link href="https://fonts.googleapis.com/css2?family=Arimo:wght@400;700&family=PT+Sans:wght@400;700&display=swap" rel="stylesheet">
<style>
  :root {
    --white: #ffffff;
    --teal: #17a9a3;
    --slate-dark: #2f393b;
    --slate-mid: #424d4f;
    --slate-light: #56605f;
    --body-text: #5a5a5a;
    --quote-grey: #e4e4e4;
    --card-border: #2a2a2a;
    --photo-light: #f3f3f3;
  }
  * { margin: 0; padding: 0; box-sizing: border-box; }
  html, body { width: 1200px; height: 900px; overflow: hidden; background: var(--white); }
  body { position: relative; font-family: "PT Sans", sans-serif; }

  .team-portrait {
    position: absolute; left: 442px; top: 0; width: 316px; height: 144px;
    background: linear-gradient(180deg, var(--photo-light) 0%, var(--photo-light) 100%);
  }
  .team-portrait-figure {
    position: absolute; left: 22px; top: 0; width: 272px; height: 144px;
    background: linear-gradient(180deg, #1f2a36 0%, #17202a 100%);
    border-radius: 0 0 6px 6px;
  }

  .testimonials {
    position: absolute; left: 0; top: 276px; width: 1200px; height: 624px;
    background:
      radial-gradient(ellipse at 70% 40%, rgba(120,130,130,0.35) 0%, rgba(0,0,0,0) 55%),
      linear-gradient(135deg, var(--slate-dark) 0%, var(--slate-mid) 50%, var(--slate-light) 100%);
    text-align: center; color: var(--white);
  }
  .section-title {
    position: absolute; left: 0; right: 0; top: 128px;
    font-family: "Arimo", sans-serif; font-weight: 400; font-size: 32px; line-height: 40px;
  }
  .section-title .accent { color: var(--teal); }
  .title-rule {
    position: absolute; left: 582px; top: 183px; width: 36px; height: 2px; background: var(--white);
  }
  .section-lead {
    position: absolute; left: 0; right: 0; top: 204px;
    font-weight: 700; font-size: 13.5px; letter-spacing: 0.3px;
  }

  .quote-card {
    position: absolute; left: 250px; top: 281px; width: 700px; height: 155px;
    background: var(--white); border: 1px solid var(--card-border);
  }
  .quote-mark {
    position: absolute; left: 40px; top: 20px;
    font-family: Georgia, serif; font-size: 60px; line-height: 60px; color: var(--quote-grey); font-weight: 700;
  }
  .quote-text {
    position: absolute; left: 60px; right: 60px; top: 44px;
    color: var(--body-text); font-size: 13.5px; line-height: 28px;
  }

  .client-name {
    position: absolute; left: 0; right: 0; top: 451px;
    font-family: "Arimo", sans-serif; font-size: 15px; font-weight: 400;
  }
  .client-role {
    position: absolute; left: 0; right: 0; top: 475px;
    font-size: 12px; color: var(--teal);
  }

  .client-avatars { position: absolute; top: 518px; left: 490px; display: flex; gap: 13px; }
  .client-avatar {
    width: 65px; height: 65px; border-radius: 50%; border: 2px solid var(--white);
    background: linear-gradient(180deg, #e9e9e9 0%, #c9c4c0 60%, #7b8894 100%);
  }

  .slider-dots { position: absolute; top: 606px; left: 580px; display: flex; gap: 3px; }
  .slider-dot { width: 8px; height: 3px; background: #d8d8d8; border-radius: 2px; }
  .slider-dot.is-active { width: 17px; background: var(--teal); }
</style>
</head>
<body>
  <div class="team-portrait" role="img" aria-label="Portrait of a team member in a dark shirt with arms crossed">
    <div class="team-portrait-figure"></div>
  </div>

  <section class="testimonials" role="region" aria-label="Client testimonials">
    <div class="testimonials-backdrop" role="img" aria-label="Overhead view of a team meeting around a desk with laptops"></div>
    <h2 class="section-title">What Our <span class="accent">Client</span> Says</h2>
    <div class="title-rule"></div>
    <p class="section-lead">The Sea Breeze soon will be making another run the Sea Breeze promises something for everyone</p>

    <blockquote class="quote-card">
      <span class="quote-mark" aria-hidden="true">&ldquo;</span>
      <p class="quote-text">They're creepy and they're kooky mysterious and spooky. They're all together ooky the Mortons What might be right world.</p>
    </blockquote>

    <p class="client-name">Jonah Brandt</p>
    <p class="client-role">Visual Designer</p>

    <div class="client-avatars">
      <div class="client-avatar" role="img" aria-label="Client photo"></div>
      <div class="client-avatar" role="img" aria-label="Client photo"></div>
      <div class="client-avatar" role="img" aria-label="Client photo"></div>
    </div>

    <div class="slider-dots" aria-hidden="true">
      <span class="slider-dot"></span>
      <span class="slider-dot"></span>
      <span class="slider-dot is-active"></span>
    </div>
  </section>
</body>
</html>
```